High-end Management Consulting Website

I am looking for a design that feels very high end and professional and very serious feeling. I would like a site that uses a lot of white space, with colors in the blue, grey family. You can use a very small about of the orange and green in the logo, but it needs to be a very small amount.

I like images similar to a rock climber helping another one up a mountain. I would love other imagery throughout the site of mountain ranges and people making it to the top.

When you think of the feel imagine people in suites, very corporate feeling. Very much focused on helping company leadership and CEOs solve problems.

From a functionality standpoint https://ninebramwell.com has a good deal of similar content- However, I do not like the colors or the design. I like graphics on websites similar to https://www.harrowcapitalgroup.com.

I like clean with lots of white space.

The link below has all of the content and design comments. https://files.quillnet.com/doc/7QpLm3XzR8vTt2KwYh5NbD9sFgJc4EuA6oViWr0Ue/view?share=open

Target Market(s)

High end businesses and very experienced executives.

Industry/Entity Type

Consulting

Coding

Coded - Design and coding required

Number of Pages Required

5+ page

Font styles to use
Sans Serif

Colors

Designer to choose colors to be used in the design.

Requirements
Must have
• white space, blues some gray, clean feel VERY LITTLE use of accent colors.

I want to have a centered navigation bar.
I would like to have a secondary scrolling image.
Nice to have
• High end imagery that speaks to what is being said in the site.
This is not the main image I want to see but I like imagery like this for the main home page.
https://www.pixelmarrow.com/image-photo/couple-hiking-help-each-other-silhouette-731864205
Should not have
• Please do not use dated images or blocky feeling. Please also do not go overboard using the icon in the design.

```html
<!DOCTYPE html>
<html lang="en">
<head>
<meta charset="utf-8">
<title>Work With Us — Northvale Crest Partners</title>
<link rel="stylesheet" href="https://fonts.googleapis.com/css2?family=Poppins:wght@400;500;600;700;800&display=swap">
<style>
:root{
  --ink:#222222;
  --body:#333333;
  --hero:#2b2b2b;
  --hero-line:#3c3c3c;
  --orange:#f7a21b;
  --orange-deep:#f15a0a;
  --blue:#2aa8ea;
  --blue-deep:#0a7fc9;
  --green:#7cc242;
  --field:#ececec;
  --footer:#112b44;
  --footer-text:#c8d3de;
  --rule:#e3e3e3;
}
*{box-sizing:border-box;margin:0;padding:0}
html,body{width:1200px;height:3363px;overflow:hidden}
body{font-family:"Poppins",sans-serif;color:var(--body);background:#fff;position:relative}
.hero{position:absolute;left:0;top:0;width:1200px;height:592px;background:var(--hero);overflow:hidden}
.hero-map{position:absolute;left:88px;top:115px;width:1020px;height:470px;background:radial-gradient(ellipse at center,rgba(255,255,255,.06),rgba(255,255,255,0) 70%)}
.hero-rule{position:absolute;top:0;width:1px;height:592px;background:var(--hero-line)}
.hero-rule.h{height:1px;width:360px;left:840px;top:329px}
.brand{position:absolute;left:88px;top:26px;display:flex;align-items:center;gap:10px;color:#fff}
.brand-dot{width:20px;height:20px;background:var(--blue)}
.brand-name{font-weight:500;font-size:16px;letter-spacing:.5px;line-height:1.1}
.brand-name small{display:block;font-size:9px;letter-spacing:3px;text-align:center}
.nav{position:absolute;top:50px;left:362px;display:flex;gap:32px}
.nav a{color:#fff;text-decoration:none;font-size:14px;font-weight:600}
.login{position:absolute;left:1000px;top:41px;width:111px;height:40px;background:var(--orange-deep);color:#fff;font-size:13px;font-weight:600;display:flex;align-items:center;justify-content:center;gap:5px}
.hero-title{position:absolute;left:0;width:1200px;top:245px;text-align:center;color:#fff;font-size:118px;font-weight:800;line-height:1;letter-spacing:-1px}
.hero-title .o{color:var(--orange)}.hero-title .b{color:var(--blue)}.hero-title .g{color:var(--green)}
.hero-arrow{position:absolute;left:590px;top:415px}
.facet{position:absolute;left:0;top:592px;width:349px;height:570px;background:linear-gradient(135deg,#1aa3e6,#0a78c2 60%,#0f8fd8)}
.photo{position:absolute;left:89px;top:737px;width:1022px;height:570px;background:linear-gradient(120deg,#3a2e22,#8a7a66 40%,#d9d3c8 60%,#2a2a2a)}
.intro{position:absolute;left:179px;top:1385px;width:830px}
.intro h2{font-size:78px;font-weight:700;color:var(--ink);line-height:1;margin-bottom:30px;letter-spacing:-1px}
.intro p{font-size:18px;line-height:26.5px;margin-bottom:15px}
.intro p.lead{font-weight:600;color:var(--ink)}
.intro a{color:var(--blue);font-size:19px;font-weight:500}
.divider{position:absolute;left:89px;top:1998px;width:1022px;height:1px;background:var(--rule)}
.contact-title{position:absolute;left:0;width:1200px;top:2126px;text-align:center;font-size:86px;font-weight:700;color:var(--ink);line-height:1}
.form{position:absolute;left:243px;top:2251px;width:713px;display:grid;grid-template-columns:351px 351px;gap:13px 11px}
.field{height:55px;background:var(--field);display:flex;align-items:center;justify-content:space-between;padding:0 24px;font-size:17px;color:#333}
.field.message{grid-column:1/3;height:168px;align-items:flex-start;padding-top:20px}
.submit{position:absolute;left:474px;top:2638px;width:252px;height:55px;background:linear-gradient(90deg,var(--orange-deep),#f7931e);color:#fff;font-weight:700;font-size:20px;display:flex;align-items:center;justify-content:center}
.footer{position:absolute;left:0;top:2843px;width:1200px;height:520px;background:var(--footer);color:var(--footer-text)}
.footer-brand{position:absolute;left:88px;top:200px;display:flex;align-items:center;gap:12px;color:#fff}
.footer-brand .brand-dot{width:30px;height:30px}
.footer-brand .brand-name{font-size:26px}
.footer-brand .brand-name small{font-size:13px;letter-spacing:4px}
.col{position:absolute;top:150px}
.col h4{color:#fff;font-size:19px;font-weight:600;margin-bottom:12px}
.col li{list-style:none;font-size:14.5px;line-height:29.5px}
.col .ci{display:flex;align-items:center;gap:8px;color:#fff;font-size:17px;line-height:26px}
.subscribe{margin-top:14px;width:260px;height:48px;background:#183553;display:flex;align-items:center;justify-content:space-between;padding:0 16px;font-size:13px;color:#fff}
.foot-rule{position:absolute;left:88px;top:461px;width:1023px;height:1px;background:#2a4661}
.copy{position:absolute;left:88px;top:480px;font-size:14px;color:#fff}
.social{position:absolute;left:1016px;top:482px;display:flex;gap:26px}
.social span{width:10px;height:10px;border-radius:50%;background:#fff;display:block}
.to-top{position:absolute;left:1128px;top:428px;width:38px;height:38px;border-radius:50%;background:var(--blue);display:flex;align-items:center;justify-content:center}
</style>
</head>
<body>
<header class="hero">
  <div class="hero-map" role="img" aria-label="Faint dotted world map"></div>
  <div class="hero-rule" style="left:263px"></div>
  <div class="hero-rule" style="left:494px"></div>
  <div class="hero-rule" style="left:771px"></div>
  <div class="hero-rule h"></div>
  <div class="brand"><span class="brand-dot"></span><div class="brand-name">NORTHVALE CREST<small>PARTNERS</small></div></div>
  <nav class="nav"><a>HOME</a><a>ABOUT</a><a>PARTNERS</a><a>EXPERIENCE</a><a>HOW WE HELP</a><a>CONTACT</a></nav>
  <div class="login"><svg width="10" height="11" viewBox="0 0 10 11"><circle cx="5" cy="3" r="2.6" fill="#fff"/><path d="M0 11c0-3 2-5 5-5s5 2 5 5z" fill="#fff"/></svg>LOGIN</div>
  <h1 class="hero-title"><span class="o">W</span>ork <span class="b">W</span>ith <span class="g">U</span>s</h1>
  <svg class="hero-arrow" width="20" height="110" viewBox="0 0 20 110"><path d="M10 0v106M3 98l7 8 7-8" stroke="#fff" stroke-width="2" fill="none"/></svg>
</header>

<div class="facet" role="img" aria-label="Blue faceted geometric panel"></div>
<div class="photo" role="img" aria-label="Consultants reviewing charts on a clipboard beside a laptop"></div>

<section class="intro">
  <h2>Work With Us</h2>
  <p>As fellow investors and industry leaders, we believe the expertise, knowledge and connections built throughout one’s career has value. Too often executives leave prominent roles or founders sell companies only to become free advisors. While giving back is important, your time has value.</p>
  <p>We provide industry leaders with short and long-term consulting and advisory roles. We provide an opportunity to stay engaged and active within one’s industry, on terms which they define. Providing flexibility which has been so hard earned.</p>
  <p>Our engagements range from hourly advisor-lead strategy sessions and defined strategy engagements to interim, permanent and board executive placements.</p>
  <p class="lead">From start-ups to global corporations, we help our advisors deliver game-changing results.</p>
  <a>Learn more about our advisor selection process.</a>
</section>

<div class="divider"></div>
<h2 class="contact-title">Contact Us</h2>
<div class="form">
  <div class="field">First Name</div><div class="field">Last Name</div>
  <div class="field">Email</div><div class="field">Phone</div>
  <div class="field">State<svg width="12" height="8" viewBox="0 0 12 8"><path d="M1 1l5 5 5-5" stroke="#333" stroke-width="2" fill="none"/></svg></div>
  <div class="field">Type<svg width="12" height="8" viewBox="0 0 12 8"><path d="M1 1l5 5 5-5" stroke="#333" stroke-width="2" fill="none"/></svg></div>
  <div class="field message">Messsage</div>
</div>
<div class="submit">SUBMIT NOW</div>

<footer class="footer">
  <div class="footer-brand"><span class="brand-dot"></span><div class="brand-name">NORTHVALE CREST<small>PARTNERS</small></div></div>
  <div class="col" style="left:436px"><h4>Useful links</h4><ul><li>Home</li><li>About</li><li>Partners</li><li>Experience</li><li>How We Help</li><li>Contact</li></ul></div>
  <div class="col" style="left:626px"><h4>Respondents</h4><ul><li>Refer Friends</li><li>Sign Up</li><li>Log In</li><li>FAQ</li></ul></div>
  <div class="col" style="left:829px"><h4>Contact Us</h4>
    <div class="ci"><svg width="10" height="13" viewBox="0 0 10 13"><path d="M5 0a5 5 0 0 0-5 5c0 4 5 8 5 8s5-4 5-8a5 5 0 0 0-5-5z" fill="#2aa8ea"/><circle cx="5" cy="5" r="2" fill="#112b44"/></svg>Info@example.com</div>
    <div class="ci"><svg width="12" height="12" viewBox="0 0 12 12"><path d="M2 0l3 3-1.5 2a7 7 0 0 0 3.5 3.5L9 7l3 3-2 2C5 12 0 7 0 2z" fill="#2aa8ea"/></svg>+08 123 456 7890</div>
    <div class="ci"><svg width="12" height="10" viewBox="0 0 12 10"><rect width="12" height="10" fill="#2aa8ea"/><path d="M0 0l6 5 6-5" stroke="#112b44" fill="none"/></svg>Info@example.com</div>
    <div class="subscribe"><span>✉&nbsp;&nbsp;&nbsp;Enter your email</span><svg width="13" height="13" viewBox="0 0 13 13"><path d="M13 0L0 6l5 2 2 5z" fill="#fff"/></svg></div>
  </div>
  <div class="to-top"><svg width="12" height="14" viewBox="0 0 12 14"><path d="M6 14V2M1 7l5-5 5 5" stroke="#fff" stroke-width="1.6" fill="none"/></svg></div>
  <div class="foot-rule"></div>
  <div class="copy">© Copyright All Rights Reserved</div>
  <div class="social"><span></span><span></span><span></span></div>
</footer>
</body>
</html>
```